*YO!!! Designers Needed!!* Front Page Cover Needed for a $$Billion Dollar$$ Company

We are a manufacturer of aluminum electrolytic capacitors. We are looking to create a front page cover that will be used on our annual report. We are a publicly listed company and work with many Brellmont 500 companies, so your work will be viewed by the BIG GUNS and EXECUTIVES around the WORLD! If selected, you may be selected for additional work.

The front page cover should be unique. If elegance, modern, bling, and creativity somehow got together and had a child, that's what the cover page would look like!

Inspired Examples attached. Check them out!

www.kovantro.com

Font styles to use
Sans Serif

Requirements
Must have
• 1. Must include the attached logo. Logo size, color, and placement are at your discretion.

2. Should include the text, '2020 Annual Report'

3. The design should incorporate the use of foil and/or be embossed. The foil can be part of the design or can be the full page. See various examples attached for reference.

4. Shall be in A4 size and vertical orientation.
Nice to have
• Feel free to add any icons or stock photos (for example capacitors or circuit boards) if needed.

Be creative here and don't be afraid to be bold! The end product will be printed and budget is not a limiting factor, so feel free to make it extravagant if needed.

Our slogan is "Think Ahead". This slogan can or cannot be part of the theme.

```html
<!DOCTYPE html>
<html lang="en">
<head>
<meta charset="utf-8">
<title>Kovantro 2020 Annual Report Cover</title>
<link href="https://fonts.googleapis.com/css2?family=Jost:wght@300;400;500&display=swap" rel="stylesheet">
<style>
  :root {
    --stage: #c8c9cb;
    --cover-deep: #1b4d6b;
    --cover-mid: #27678a;
    --cover-light: #3f86a8;
    --cover-glow: #5a9cb9;
    --ink-white: #ffffff;
    --foil-silver: #dfe7ec;
    --slogan: rgba(160, 198, 216, 0.36);
    --emboss-light: rgba(255, 255, 255, 0.22);
    --emboss-dark: rgba(5, 30, 48, 0.45);
  }
  * { margin: 0; padding: 0; box-sizing: border-box; }
  html, body {
    width: 1200px;
    height: 960px;
    overflow: hidden;
    background: var(--stage);
    font-family: "Jost", "Futura", sans-serif;
  }
  .canvas {
    position: relative;
    width: 1200px;
    height: 960px;
  }
  .cover {
    position: absolute;
    left: 252px;
    top: 28px;
    width: 696px;
    height: 904px;
    overflow: hidden;
    box-shadow: 0 8px 20px rgba(0, 0, 0, 0.28);
  }
  .cover-photo {
    position: absolute;
    inset: 0;
    background:
      radial-gradient(ellipse 38% 26% at 62% 36%, var(--cover-glow) 0%, rgba(90,156,185,0) 100%),
      radial-gradient(ellipse 55% 40% at 78% 20%, var(--cover-light) 0%, rgba(63,134,168,0) 100%),
      radial-gradient(ellipse 45% 30% at 20% 10%, rgba(63,134,168,0.7) 0%, rgba(63,134,168,0) 100%),
      radial-gradient(ellipse 60% 35% at 30% 62%, rgba(27,77,107,0.55) 0%, rgba(27,77,107,0) 100%),
      linear-gradient(170deg, var(--cover-mid) 0%, var(--cover-mid) 50%, var(--cover-deep) 100%);
  }
  .foil-sheen {
    position: absolute;
    inset: 0;
    background: linear-gradient(125deg,
      rgba(255,255,255,0) 30%,
      rgba(255,255,255,0.07) 42%,
      rgba(255,255,255,0) 54%);
  }
  .brand-name {
    position: absolute;
    top: 34px;
    right: 56px;
    color: var(--ink-white);
    font-weight: 500;
    font-size: 80px;
    line-height: 1;
  }
  .slogan {
    position: absolute;
    left: 26px;
    bottom: 88px;
    writing-mode: vertical-rl;
    transform: rotate(180deg);
    color: var(--slogan);
    font-weight: 300;
    font-size: 110px;
    line-height: 1;
    letter-spacing: 4px;
    white-space: nowrap;
    text-shadow:
      1px 1px 0 var(--emboss-light),
      -1px -1px 1px var(--emboss-dark);
  }
  .report-title {
    position: absolute;
    right: 56px;
    bottom: 34px;
    text-align: right;
    font-weight: 400;
  }
  .report-year {
    display: block;
    font-size: 106px;
    line-height: 0.95;
    letter-spacing: 2px;
    background: linear-gradient(180deg, var(--ink-white) 0%, var(--foil-silver) 55%, var(--ink-white) 100%);
    -webkit-background-clip: text;
    background-clip: text;
    color: transparent;
    filter: drop-shadow(1px 2px 1px var(--emboss-dark));
  }
  .report-label {
    display: block;
    color: var(--ink-white);
    font-size: 29px;
    letter-spacing: 1.5px;
    margin-top: 2px;
    text-shadow: 1px 1px 1px var(--emboss-dark);
  }
</style>
</head>
<body>
  <main class="canvas">
    <section class="cover">
      <div class="cover-photo" role="img" aria-label="Close-up photograph of a blue printed circuit board with traces and solder pads, brightest toward the upper right"></div>
      <div class="foil-sheen"></div>
      <div class="brand-name">Kovantro</div>
      <div class="slogan">THINK AHEAD</div>
      <h1 class="report-title">
        <span class="report-year">2020</span>
        <span class="report-label">ANNUAL REPORT</span>
      </h1>
    </section>
  </main>
</body>
</html>
```